Summer Sale Graphics for Social Media

I want to create 11 social media graphics (new Instagram size 4:5 (1080 x 1350 pixels) focusing on our Summer Sale Graphics, using any of the pics attached. Use the attached pics, NO RANDOM STOCK PHOTOGRAPHY. For the color scheme of the graphics, they should all be complementary to the product colors in the photos.
You can add any of the photos attached but none are required. You can do some of the graphics in all text. I mainly need BOLD text that says one of the headlines (11 total) SEE ATTACHED WORD DOCUMENT for the headlines to use.

```html
<!DOCTYPE html>
<html lang="en">
<head>
<meta charset="utf-8">
<title>Summer Sale Social Graphics</title>
<link href="https://fonts.googleapis.com/css2?family=Montserrat:wght@300;400;800;900&display=swap" rel="stylesheet">
<style>
  :root {
    --ink: #2b2b2b;
    --brand-grey: #5b5b5b;
    --frame: #d6d6d6;
    --table-light: #f1f0ee;
    --table-dark: #dedcd9;
    --blue: #4a8ff0;
    --coral: #f26b5b;
    --teal: #5a8f7b;
    --red: #c0282d;
    --purple: #6a12a6;
    --pink: #f57fa4;
    --green: #7ed957;
    --yellow: #f5d300;
    --royal: #1230e8;
    --orange: #ff6a00;
    --magenta: #8b1a8b;
  }
  * { box-sizing: border-box; margin: 0; padding: 0; }
  html, body { width: 1200px; height: 1097px; overflow: hidden; background: #fff; }
  body { position: relative; font-family: "Montserrat", Arial, sans-serif; color: var(--ink); }

  .ad {
    position: absolute; width: 216px; height: 270px;
    background: #fff; border: 1px solid var(--frame); overflow: hidden;
  }
  .rings { position: absolute; inset: 0; width: 216px; height: 270px; color: var(--accent); opacity: .3; }

  .brand {
    position: absolute; left: 17px; top: 16px; display: flex; align-items: center; gap: 4px;
    font-weight: 900; font-size: 19px; letter-spacing: -.3px; color: var(--brand-grey);
  }
  .brand i { display: block; width: 12px; height: 14px; background: var(--accent); }

  .photo {
    position: absolute; left: 128px; top: 12px; width: 88px; height: 218px;
    border-radius: 34px 0 0 0;
    background: linear-gradient(180deg,
      #3a2c26 0%, #6b4a3a 16%, #efe9e6 30%, #ffffff 46%,
      #a57458 56%, #8a5c44 62%, #2a2a2e 72%, #1d1d21 100%);
    opacity: .85;
  }
  .table {
    position: absolute; left: 0; top: 228px; width: 216px; height: 42px;
    background: linear-gradient(180deg, var(--table-light), var(--table-dark));
  }
  .table::after {
    content: ""; position: absolute; left: 138px; top: -20px; width: 42px; height: 38px;
    background: linear-gradient(90deg, #f6f6f8 0 45%, transparent 45% 55%, #f3eef4 55%);
    border-radius: 5px 5px 2px 2px;
  }

  .copy {
    position: absolute; left: 21px; width: 120px;
    font-size: 11px; line-height: 1.02; font-weight: 400; color: var(--ink);
  }
  .copy b { font-weight: 900; }
  .copy .hot { color: var(--accent); font-weight: 900; }
  .copy .dark { font-weight: 900; color: var(--ink); }
  .copy.small { font-size: 9px; }
  .copy p + p { margin-top: 8px; }

  .cta {
    position: absolute; left: 21px; padding: 3px 6px;
    background: var(--accent); color: #fff; border-radius: 3px;
    font-size: 7.5px; font-weight: 800; letter-spacing: .3px;
  }

  .deal { position: absolute; left: 21px; top: 207px; width: 34px; height: 34px; }
  .deal .usd {
    position: absolute; left: 0; top: 0; width: 9px; height: 9px; background: #111;
    color: #fff; font-size: 6px; line-height: 9px; text-align: center;
  }
  .deal .num {
    position: absolute; left: 0; top: 6px; width: 34px; height: 28px; background: var(--accent);
    color: #fff; font-weight: 800; font-size: 24px; line-height: 28px; text-align: center; letter-spacing: -1.5px;
  }
  .deal .off {
    position: absolute; right: -2px; bottom: -4px; padding: 1px 2px; background: #111;
    color: #fff; font-size: 6px; line-height: 7px;
  }
</style>
</head>
<body>

<svg width="0" height="0" style="position:absolute">
  <defs>
    <g id="ring-set" fill="none" stroke="currentColor" stroke-linecap="round">
      <circle cx="76" cy="140" r="92" stroke-width="5"/>
      <path d="M76 62 A78 78 0 0 0 -2 140" stroke-width="5"/>
      <path d="M76 80 A60 60 0 0 0 16 140" stroke-width="5"/>
    </g>
  </defs>
</svg>

<!-- Row 1 -->
<article class="ad" style="--accent: var(--blue); left:110px; top:112px;">
  <svg class="rings" viewBox="0 0 216 270"><use href="#ring-set"/></svg>
  <div class="photo" role="img" aria-label="Smiling woman in a white crop top holding a supplement bottle"></div>
  <div class="table" role="img" aria-label="Marble tabletop with two supplement bottles"></div>
  <span class="brand"><i></i>SUNFIT</span>
  <div class="copy" style="top:116px;">Your<br><b>Summer Body</b><br><span class="hot">Won’t Wait</span></div>
  <span class="cta" style="top:163px;">SALE NOW!</span>
  <div class="deal"><span class="usd">$</span><span class="num">15</span><span class="off">OFF</span></div>
</article>

<article class="ad" style="--accent: var(--coral); left:366px; top:112px;">
  <svg class="rings" viewBox="0 0 216 270"><use href="#ring-set"/></svg>
  <div class="photo" role="img" aria-label="Smiling woman in a white crop top holding a supplement bottle"></div>
  <div class="table" role="img" aria-label="Marble tabletop with two supplement bottles"></div>
  <span class="brand"><i></i>SUNFIT</span>
  <div class="copy" style="top:117px;">Final<br><b>Countdown</b><br><span class="hot">to Summer</span></div>
  <span class="cta" style="top:163px;">SALE NOW!</span>
  <div class="deal"><span class="usd">$</span><span class="num">15</span><span class="off">OFF</span></div>
</article>

<article class="ad" style="--accent: var(--teal); left:620px; top:112px;">
  <svg class="rings" viewBox="0 0 216 270"><use href="#ring-set"/></svg>
  <div class="photo" role="img" aria-label="Smiling woman in a white crop top holding a supplement bottle"></div>
  <div class="table" role="img" aria-label="Marble tabletop with two supplement bottles"></div>
  <span class="brand"><i></i>SUNFIT</span>
  <div class="copy small" style="top:116px; left:19px; width:110px;">• <span class="hot">Detox,</span><br>• <span class="hot">Burn Fat,</span><br>• and <span class="hot">Turn Heads</span><br>&nbsp;&nbsp;<span class="hot">This Summer</span></div>
  <span class="cta" style="top:163px;">SALE NOW!</span>
  <div class="deal"><span class="usd">$</span><span class="num">15</span><span class="off">OFF</span></div>
</article>

<article class="ad" style="--accent: var(--red); left:873px; top:112px;">
  <svg class="rings" viewBox="0 0 216 270"><use href="#ring-set"/></svg>
  <div class="photo" role="img" aria-label="Smiling woman in a white crop top holding a supplement bottle"></div>
  <div class="table" role="img" aria-label="Marble tabletop with two supplement bottles"></div>
  <span class="brand"><i></i>SUNFIT</span>
  <div class="copy small" style="top:127px; width:100px;">Summer’s Here.<br>And We’re Having<br>the <span class="hot">BIGGEST SALE</span><br>of the Year</div>
  <div class="deal"><span class="usd">$</span><span class="num">15</span><span class="off">OFF</span></div>
</article>

<!-- Row 2 -->
<article class="ad" style="--accent: var(--purple); left:110px; top:425px;">
  <svg class="rings" viewBox="0 0 216 270"><use href="#ring-set"/></svg>
  <div class="photo" role="img" aria-label="Smiling woman in a white crop top holding a supplement bottle"></div>
  <div class="table" role="img" aria-label="Marble tabletop with two supplement bottles"></div>
  <span class="brand"><i></i>SUNFIT</span>
  <div class="copy" style="top:123px;">One <span class="hot">SALE.</span><br>One <span class="hot">Body.</span><br>One <span class="hot">Summer</span><br><span class="hot">to Slay</span></div>
  <div class="deal"><span class="usd">$</span><span class="num">15</span><span class="off">OFF</span></div>
</article>

<article class="ad" style="--accent: var(--pink); left:366px; top:425px;">
  <svg class="rings" viewBox="0 0 216 270"><use href="#ring-set"/></svg>
  <div class="photo" role="img" aria-label="Smiling woman in a white crop top holding a supplement bottle"></div>
  <div class="table" role="img" aria-label="Marble tabletop with two supplement bottles"></div>
  <span class="brand"><i></i>SUNFIT</span>
  <div class="copy small" style="top:121px;"><p>Summer Isn’t<br>Waiting</p><p><span class="hot">Neither<br>Should You</span></p></div>
  <span class="cta" style="top:173px;">SALE NOW!</span>
  <div class="deal"><span class="usd">$</span><span class="num">15</span><span class="off">OFF</span></div>
</article>

<article class="ad" style="--accent: var(--green); left:620px; top:425px;">
  <svg class="rings" viewBox="0 0 216 270"><use href="#ring-set"/></svg>
  <div class="photo" role="img" aria-label="Smiling woman in a white crop top holding a supplement bottle"></div>
  <div class="table" role="img" aria-label="Marble tabletop with two supplement bottles"></div>
  <span class="brand"><i></i>SUNFIT</span>
  <div class="copy" style="top:117px;"><p>Slim <span class="hot">Waist.</span><br>Flat <span class="hot">Tummy.</span><br>More <span class="hot">Energy.</span></p><p><i><span class="dark">Let’s</span> <span class="hot">Go!</span></i></p></div>
  <span class="cta" style="top:176px;">SALE NOW!</span>
  <div class="deal"><span class="usd">$</span><span class="num">15</span><span class="off">OFF</span></div>
</article>

<article class="ad" style="--accent: var(--yellow); left:873px; top:425px;">
  <svg class="rings" viewBox="0 0 216 270"><use href="#ring-set"/></svg>
  <div class="photo" role="img" aria-label="Smiling woman in a white crop top holding a supplement bottle"></div>
  <div class="table" role="img" aria-label="Marble tabletop with two supplement bottles"></div>
  <span class="brand"><i></i>SUNFIT</span>
  <div class="copy small" style="top:121px; width:100px;"><p><span class="hot">Hurry!</span></p><p>Our Summer Slim<br>Down <span class="hot">SALE</span> Is On<br><span class="hot">Don’t Miss It!</span></p></div>
  <span class="cta" style="top:173px;">SALE NOW!</span>
  <div class="deal"><span class="usd">$</span><span class="num">15</span><span class="off">OFF</span></div>
</article>

<!-- Row 3 -->
<article class="ad" style="--accent: var(--royal); left:185px; top:730px;">
  <svg class="rings" viewBox="0 0 216 270"><use href="#ring-set"/></svg>
  <div class="photo" role="img" aria-label="Smiling woman in a white crop top holding a supplement bottle"></div>
  <div class="table" role="img" aria-label="Marble tabletop with two supplement bottles"></div>
  <span class="brand"><i></i>SUNFIT</span>
  <div class="copy" style="top:126px; font-size:10px;"><span class="hot">SALE</span><br>Your Summer<br>Body Starts Here</div>
  <div class="deal"><span class="usd">$</span><span class="num">15</span><span class="off">OFF</span></div>
</article>

<article class="ad" style="--accent: var(--orange); left:499px; top:730px;">
  <svg class="rings" viewBox="0 0 216 270"><use href="#ring-set"/></svg>
  <div class="photo" role="img" aria-label="Smiling woman in a white crop top holding a supplement bottle"></div>
  <div class="table" role="img" aria-label="Marble tabletop with two supplement bottles"></div>
  <span class="brand"><i></i>SUNFIT</span>
  <div class="copy small" style="top:132px; width:110px;"><p>Limited-<span class="hot">Time</span><br>Summer <span class="hot">SALE</span></p><p><span class="hot">Snatch</span> Your<br><span class="hot">Supplements Now!</span></p></div>
  <div class="deal"><span class="usd">$</span><span class="num">15</span><span class="off">OFF</span></div>
</article>

<article class="ad" style="--accent: var(--magenta); left:798px; top:730px;">
  <svg class="rings" viewBox="0 0 216 270"><use href="#ring-set"/></svg>
  <div class="photo" role="img" aria-label="Smiling woman in a white crop top holding a supplement bottle"></div>
  <div class="table" role="img" aria-label="Marble tabletop with two supplement bottles"></div>
  <span class="brand"><i></i>SUNFIT</span>
  <div class="copy small" style="top:124px; width:100px;"><p>Get Snatched for<br>Summer</p><p><span class="hot">Supplements</span><br>On <span class="hot">SALE NOW!</span></p></div>
  <span class="cta" style="top:179px;">SALE NOW!</span>
  <div class="deal"><span class="usd">$</span><span class="num">15</span><span class="off">OFF</span></div>
</article>

</body>
</html>
```